CD Cover (Falt-Karton-Cover: siehe Beispiel) für Sängerin
Zielgruppe
Es handelt sich um eine Musik-CD einer Sängerin aus der Kirtan/Yoga Szene.
Musik Beispiele ihrer zweiten Band sind in den Links zu finden, um es sich Vorstellen zu können.
Die Zielgruppe ist also sehr breit. Grundsätzlich kann man sagen, alle die etwas mit Yoga und Musik anfangen können.
Aufgabenstellung
KURZÜBERBLICK (Dateien):
Für das faltbare Cover aus Karton und die darin enthaltene CD benötige ich ein Design.
Optisch soll es so Wirken: frisch, glücklich, feminin
Ich habe bereits eine grobes Design beigefügt, wie ich es mit der Sängerin besprochen habe (Roughcover_Idee.jpg).
Es stellt nur eine grobe Übersicht dar, wie wir uns das ungefähr vorstellen. Draus soll nun ein schönes harmonisches Cover entstehen.
Die Hintergrundfarbe kann angepasst werden oder andere Vorschläge gemacht werden. Ein Grün habe ich mal so besprochen mit der Sängerin, da es mit den Bildern zusammenpasst. Grundsätzlich bin ich natürlich froh um kreative Vorschläge. Die Hintergrundfarbe kann ich mir auch gut als "Aquarell" oder sonstiges sanftes Muster vorstellen. Dazu einige geschwungene Ornamente/Formen als Haarlinien oder ähnliche Dekoelemente.
Das Cover soll nicht überladen wirken, sondern warm aber aufgeräumt, also nicht trashig.
Texte:
Bilder:
- als RAW
- als JPG
Logos:
- als EPS "KAVTO"
- Das MURELDA Logo folgt noch.
Das Dateiformat bitte Illustrator oder InDesign, resp. gut zum Druck PDF.
Gut zum Druck bis spätestens Donnerstag Abend 12 September 2013.

```html
<!DOCTYPE html>
<html lang="en">
<head>
<meta charset="utf-8">
<title>velOrina – chants of love &amp; joy – disc label</title>
<link rel="stylesheet" href="https://fonts.googleapis.com/css2?family=Dancing+Script:wght@500;600&family=Source+Sans+3:wght@400&display=swap">
<style>
  :root {
    --paper: #ffffff;
    --leaf: #7a961c;
    --leaf-deep: #5a8224;
    --leaf-pale: #c3d193;
    --sand: #c9c39a;
    --berry: #8e0a52;
    --ink-light: #ffffff;
  }
  html, body {
    margin: 0;
    padding: 0;
    width: 1200px;
    height: 848px;
    overflow: hidden;
    background: var(--paper);
  }
  .canvas {
    position: relative;
    width: 1200px;
    height: 848px;
  }
  .disc-label {
    position: absolute;
    left: 0;
    top: 0;
  }
  .title-arc {
    font-family: "Dancing Script", cursive;
  }
  .title-arc.album { fill: var(--berry); font-size: 27px; font-weight: 500; }
  .title-arc.artist { fill: var(--ink-light); font-size: 28px; font-weight: 600; }
  .title-arc.guest { fill: var(--ink-light); font-size: 20px; font-weight: 500; }
  .credits-arc {
    font-family: "Source Sans 3", sans-serif;
    font-size: 8px;
    fill: var(--ink-light);
  }
  .distributor-mark { fill: var(--paper); }
</style>
</head>
<body>
<main class="canvas">
  <svg class="disc-label" width="1200" height="848" viewBox="0 0 1200 848" xmlns="http://www.w3.org/2000/svg">
    <defs>
      <linearGradient id="discWash" x1="0" y1="0.3" x2="1" y2="0.8">
        <stop offset="0" stop-color="var(--leaf-deep)"/>
        <stop offset="0.35" stop-color="var(--leaf)"/>
        <stop offset="0.75" stop-color="#7f981f"/>
        <stop offset="1" stop-color="#9ea85c"/>
      </linearGradient>
      <radialGradient id="sandCorner" cx="0.82" cy="0.9" r="0.35">
        <stop offset="0" stop-color="var(--sand)" stop-opacity="0.7"/>
        <stop offset="1" stop-color="var(--sand)" stop-opacity="0"/>
      </radialGradient>
      <radialGradient id="mandalaTone" cx="0.5" cy="0.5" r="0.5">
        <stop offset="0.3" stop-color="var(--leaf-pale)" stop-opacity="0"/>
        <stop offset="0.45" stop-color="var(--leaf-pale)" stop-opacity="0.35"/>
        <stop offset="0.8" stop-color="var(--leaf-pale)" stop-opacity="0.4"/>
        <stop offset="1" stop-color="var(--leaf-pale)" stop-opacity="0"/>
      </radialGradient>
      <path id="titlePath" d="M422.8 351.5 A197 197 0 1 1 736.2 571.8"/>
      <path id="creditsPath" d="M403.5 467 A207 207 0 0 0 670 620.9"/>
    </defs>

    <g class="disc">
      <circle cx="606" cy="424" r="237" fill="url(#discWash)"/>
      <circle cx="606" cy="424" r="237" fill="url(#sandCorner)"/>
      <circle class="mandala" role="img" aria-label="Hand-drawn pale green flower mandala with looped petals around the centre"
              cx="606" cy="424" r="180" fill="url(#mandalaTone)"/>
      <circle class="spindle-hole" cx="606" cy="424" r="44" fill="var(--paper)"/>
    </g>

    <text class="title-arc album"><textPath href="#titlePath" startOffset="0" textLength="352" lengthAdjust="spacingAndGlyphs">velOrina chants of love &amp; joy</textPath></text>
    <text class="title-arc artist"><textPath href="#titlePath" startOffset="362" textLength="142" lengthAdjust="spacingAndGlyphs">Lorena Imhof</textPath></text>
    <text class="title-arc guest"><textPath href="#titlePath" startOffset="512" textLength="196" lengthAdjust="spacingAndGlyphs">with Bhajan Aurel Vogt</textPath></text>

    <text class="credits-arc"><textPath href="#creditsPath" startOffset="0" textLength="425" lengthAdjust="spacingAndGlyphs">Produced by Lorena Imhof &amp; Bhajan Aurel Vogt 2013 © Lorena Imhof, lumi-yoga.ch | 7LUX.ch, Distributed by</textPath></text>

    <rect class="distributor-mark" x="680" y="593.5" width="48" height="11" transform="rotate(-29 704 599)"/>
  </svg>
</main>
</body>
</html>
```